Interimsmanager sucht Design
Zielgruppe
Erbringen von Dienstleistungen in Form Interimsmanagement in Krankenhäusern in den Bereichen IT, Medizintechnik, Projektmanagement
Zielgruppe: Vorstände, Bereichsleiter, Entscheider für IT und Medizintechnik und Kosten
Branchen: Krankenhäuser, IT, Dienstleistung
Aufgabenstellung
1) Flyer DIN A 4 6seitig (2-Bruch-Wickel-Falz)
2) Texte und grobe Layout-Vorgabe in anhängendem PDF (siehe auch 6)
3) erforderliche Fotos z.B. aus Portalen wie Bildora Platzhalter/Preview einsetzen, die Lizenzen werden dann von mir gekauft
4) Alternativ-Vorschläge bei Bildauswahl willkommen
5) 1 Profilbild je nach Platz/Layout einbauen
6) Logo-Vorlage in diversen Formaten, kann auch noch für 300dpi aufbereitet werden (derzeit noch nicht vorhanden)
6) anhängendes Dokument gibt nur grob vor, wie so etwas aussehen könnte - Alternativ-Vorschläge willkommen

```html
<!DOCTYPE html>
<html lang="de">
<head>
<meta charset="utf-8">
<title>Veltrano – Interimsmanagement Flyer</title>
<link href="https://fonts.googleapis.com/css2?family=Roboto:wght@300;400;700&family=Roboto+Condensed:wght@700&display=swap" rel="stylesheet">
<style>
  :root {
    --stage: #e4e4e4;
    --paper: #f7f7f7;
    --paper-shade: #e2e2e2;
    --blue: #1d6aa8;
    --blue-deep: #0f4f86;
    --band: #1b4d5e;
    --accent: #4b97c8;
    --ink: #2b2f33;
    --white: #ffffff;
    --photo-a: #8a8f96;
    --photo-b: #c9ccd0;
  }
  * { box-sizing: border-box; margin: 0; padding: 0; }
  html, body { width: 1200px; height: 900px; overflow: hidden; }
  body {
    background: var(--stage);
    font-family: "Roboto", Arial, sans-serif;
    color: var(--ink);
  }
  .flyer {
    position: absolute;
    left: 45px; top: 57px;
    width: 1110px; height: 785px;
    display: flex;
    box-shadow: 0 8px 28px rgba(0,0,0,.18);
  }
  .panel { width: 370px; height: 100%; position: relative; }

  /* Cover panel */
  .panel--cover { background: linear-gradient(180deg, var(--blue) 0%, var(--blue-deep) 100%); color: var(--white); }
  .cover-photo {
    height: 205px;
    background: linear-gradient(135deg, var(--photo-b) 0%, var(--photo-a) 100%);
  }
  .brand-band {
    position: absolute; left: 0; top: 168px;
    width: 100%; height: 66px;
    background: var(--band);
    display: flex; align-items: center; gap: 12px;
    padding-left: 26px;
  }
  .brand-dot { width: 22px; height: 22px; border-radius: 50%; background: var(--white); }
  .brand-name { font-size: 34px; font-weight: 400; letter-spacing: .5px; color: var(--white); }
  .cover-body { padding: 44px 26px 0 26px; }
  .cover-title { font-size: 22px; font-weight: 300; line-height: 1.2; }
  .cover-lead { font-size: 12.5px; font-weight: 700; line-height: 1.35; margin-top: 8px; }
  .cover-question { font-size: 21px; font-weight: 300; line-height: 1.2; margin-top: 30px; opacity: .85; }
  .benefits { list-style: none; margin-top: 22px; }
  .benefits li { font-size: 12px; line-height: 1.35; margin-bottom: 9px; padding-left: 12px; position: relative; }
  .benefits li::before { content: "•"; position: absolute; left: 0; }

  /* Inner panels */
  .panel--inner { background: linear-gradient(90deg, var(--paper-shade) 0%, var(--paper) 18%, var(--white) 60%, var(--paper) 100%); padding: 150px 28px 0 30px; }
  .headline {
    position: absolute; left: 400px; top: 30px; width: 680px;
    font-size: 30px; font-weight: 300; line-height: 1.12;
    text-transform: uppercase; color: var(--accent); letter-spacing: .5px;
  }
  .section-title { font-size: 20px; font-weight: 300; line-height: 1.2; color: var(--accent); }
  .section-title--lead { color: var(--blue-deep); }
  .group-title { font-size: 17px; font-weight: 300; color: var(--accent); margin: 24px 0 10px; line-height: 1.2; }
  .items { list-style: none; }
  .items li { font-size: 11.5px; line-height: 1.35; margin-bottom: 7px; padding-left: 11px; position: relative; }
  .items li::before { content: "•"; position: absolute; left: 0; color: var(--accent); }
  .items .sub { list-style: none; margin-top: 2px; }
  .items .sub li { margin-bottom: 1px; }
  .items .sub li::before { content: "–"; }
  .contact { margin-top: 34px; font-family: "Roboto Condensed", Arial, sans-serif; font-weight: 700; font-size: 13px; line-height: 1.35; color: var(--ink); }
  .contact-phone { margin-top: 14px; }
</style>
</head>
<body>
  <div class="flyer">
    <section class="panel panel--cover">
      <div class="cover-photo" role="img" aria-label="Foto: Geschäftsleute im Gespräch und Profilbild einer lächelnden Frau"></div>
      <div class="brand-band">
        <span class="brand-dot"></span>
        <span class="brand-name">Veltrano</span>
      </div>
      <div class="cover-body">
        <h1 class="cover-title">Interimsmanagement in IT<br>und Medizintechnik</h1>
        <p class="cover-lead">Maßgeschneiderte B2B-Lösungen für Ihr Unternehmen, um Ihre unternehmenspolitischen Zielsetzungen konsequent umzusetzen.</p>
        <h2 class="cover-question">Welche Vorteile bietet<br>Ihnen Interims Management<br>für Ihr Haus?</h2>
        <ul class="benefits">
          <li>Breit gefächerte Fachexpertise</li>
          <li>Definierte Kalkulationsrahmen ohne Belastung Ihres Headcounts und der Personalkosten</li>
          <li>Fest umrissene Kosten ohne Nachteil einer festen arbeitsvertraglichen Bindung</li>
          <li>Entlastung der Geschäftsführung</li>
          <li>Zusätzliche Ressourcen für Ihr Unternehmen</li>
          <li>Flexibilität und Effizienz</li>
          <li>Kurzfristige Verfügbarkeit</li>
          <li>Unternehmenspolitische Unabhängigkeit</li>
        </ul>
      </div>
    </section>

    <p class="headline">Expertise flexibel und<br>bedarfsgerecht zuschaltbar –<br>Fragen Sie uns!</p>

    <section class="panel panel--inner">
      <h2 class="section-title section-title--lead">Beispiele für effizientes<br>Projektmanagement</h2>
      <h3 class="group-title">Bereich IT</h3>
      <ul class="items">
        <li>Konsolidierung IT-Verträge:
          <ul class="sub">
            <li>Vereinheitlichung nach EVB-IT</li>
            <li>Bündelung reiner Einzel- in kostengünstigere Rahmenverträge</li>
            <li>Vereinbarung von SLA's</li>
          </ul>
        </li>
        <li>Geschäftsprozessanalyse klinischer und administrativer Abläufe</li>
        <li>Bedarfsermittlung zur Einführung klinischer Applikationen:
          <ul class="sub">
            <li>Nutzergespräche</li>
            <li>Analyse vorhandener Systeme (Ist-Zustand)</li>
            <li>Bedarfsermittlung z.B. für gesetzl., forensische oder abrechnungsrelevante Anforderungen (Soll-Zustand)</li>
          </ul>
        </li>
        <li>Reduzierung redundanter Einzelsysteme, Konzentration auf Etablierung eines „Führenden Systems"</li>
        <li>Vertragsverhandlungen mit Hard- &amp; Softwareanbietern</li>
      </ul>
      <h3 class="group-title">Bereich Medizintechnik</h3>
      <ul class="items">
        <li>Koordination der Inbetriebnahme MT-Geräte mit Firmen, Fachabteilung/Klinik, MT und IT</li>
        <li>Vertragsverhandlungen zur Optimierung von Wartungs- und Folgekosten</li>
      </ul>
    </section>

    <section class="panel panel--inner">
      <h2 class="section-title section-title--lead">Med.-Technik - Möglichkeiten<br>der Ausgestaltung</h2>
      <h3 class="group-title">Projekt-Koordination<br>Facilities Management (FM) -<br>IT – Medizintechnik (MT), Einkauf</h3>
      <ul class="items">
        <li>Abstimmung mit FM bei speziellen Baumaßnahmen für med.-technische Einrichtungen</li>
        <li>Begleitung von Rahmenvertragsverhandlungen für IT, MT und Einkauf (med. Verbrauchsmaterialien für MT-Geräte)</li>
      </ul>
      <h3 class="group-title">Compliance externer Dienstleister</h3>
      <ul class="items">
        <li>Abwicklung der gesamten Prozesse mit externen Dienstleistern von der
          <ul class="sub">
            <li>Auswahl,</li>
            <li>über Verhandlungsführung,</li>
            <li>Abstimmung und Koordination mit internen Abteilungen</li>
          </ul>
        </li>
      </ul>
      <div class="contact">
        <p>Haben Sie spezielle Fragestellungen?<br>Rufen Sie uns an! Wir nehmen uns Zeit für Sie!</p>
        <p class="contact-phone">Mobil 0160 555 21 874</p>
      </div>
    </section>
  </div>
</body>
</html>
```